Roost 'n run. Chicken shop

yDesign special menu with special pictures within 48 h
Very smaple menu

Target Market(s)

Local

Industry/Entity Type

Food

Colors
FFF300
FFF600
FEFA6F
FFFEC7
FFFEE8

Requirements
Must have
• IGood quality picture
Nice to have
• Good quality pictures

```html
<!DOCTYPE html>
<html lang="en">
<head>
<meta charset="utf-8">
<title>Roost 'n run – Menu</title>
<link href="https://fonts.googleapis.com/css2?family=Bebas+Neue&family=Montserrat:wght@500;600;800;900&display=swap" rel="stylesheet">
<style>
  :root{
    --bg:#FDB913;
    --ink:#121008;
    --brown:#5A3714;
    --badge:#FFF300;
    --cream:#FFFEE8;
    --glow:#FEFA6F;
  }
  *{margin:0;padding:0;box-sizing:border-box}
  html,body{width:1200px;height:849px;overflow:hidden;background:var(--bg)}
  .menu{position:relative;width:1200px;height:849px;background:var(--bg);overflow:hidden;
        font-family:"Montserrat",Arial,sans-serif;color:var(--ink)}
  .t{position:absolute;white-space:nowrap;line-height:1}
  .heading{font-family:"Bebas Neue","Arial Narrow",sans-serif;font-size:42px;letter-spacing:.5px;color:var(--ink)}
  .heading.sub{font-size:31px}
  .note{font-size:11px;font-weight:500}
  .lead{font-size:15.5px;font-weight:800}
  .lead span{font-weight:500}
  .price-row{font-size:15.5px;font-weight:500}
  .price-row b{font-weight:900}
  .item{font-size:21px;font-weight:500}
  .item b{font-weight:900}
  .desc{position:absolute;font-size:11.3px;font-weight:500;line-height:13.4px;white-space:nowrap}
  .opt{font-size:14.5px;font-weight:500}
  .opt b{font-weight:900}
  .tiny{font-size:9.5px;font-weight:500}
  .micro{position:absolute;font-size:8px;font-weight:500;line-height:9.5px}
  .badge{position:absolute;border-radius:50%;display:flex;align-items:center;justify-content:center;
         font-size:20px;font-weight:500;line-height:1}
  .badge.light{background:var(--badge);color:var(--ink)}
  .badge.dark{background:var(--brown);color:var(--cream)}
  .dots{position:absolute;display:flex;align-items:center;gap:3px}
  .dots i{display:block;border-radius:50%;background:var(--brown)}
  .dots i:nth-child(1){width:9px;height:9px}
  .dots i:nth-child(2){width:6px;height:6px}
  .dots i:nth-child(3){width:4px;height:4px}
  .brand{position:absolute;left:413px;top:44px;width:366px;text-align:center;
         font-family:"Bebas Neue","Arial Narrow",sans-serif;font-size:66px;line-height:1;color:var(--brown)}
  .art{position:absolute}
  .spot{position:absolute;border-radius:50%}
</style>
</head>
<body>
<main class="menu">

  <!-- background artwork areas -->
  <div class="art" role="img" aria-label="Faint photo of breaded chicken wings" style="left:-20px;top:-20px;width:120px;height:110px;border-radius:50%;background:radial-gradient(circle,#F3A51A 0%,rgba(253,185,19,0) 70%)"></div>
  <div class="art" role="img" aria-label="Faint photo of fried chicken pieces" style="left:460px;top:690px;width:170px;height:160px;border-radius:50%;background:radial-gradient(circle,#F0A517 0%,rgba(253,185,19,0) 70%)"></div>
  <div class="art" role="img" aria-label="Faint photo of french fries" style="left:1030px;top:640px;width:190px;height:220px;border-radius:30%;background:radial-gradient(circle,#FCC534 0%,rgba(253,185,19,0) 70%)"></div>

  <!-- decorative spots -->
  <div class="spot" style="left:325px;top:100px;width:23px;height:23px;background:var(--glow)"></div>
  <div class="spot" style="left:384px;top:19px;width:12px;height:12px;border:2.5px solid var(--cream)"></div>
  <div class="spot" style="left:410px;top:111px;width:8px;height:8px;background:var(--cream)"></div>
  <div class="spot" style="left:776px;top:20px;width:13px;height:13px;background:var(--glow)"></div>
  <div class="spot" style="left:860px;top:66px;width:8px;height:8px;background:var(--cream)"></div>

  <!-- header -->
  <div class="brand">ROOST 'N RUN</div>
  <div class="art" role="img" aria-label="Hand-lettered 'Menu' script with a fried chicken drumstick illustration"
       style="left:440px;top:104px;width:420px;height:142px;border-radius:60px;background:linear-gradient(90deg,#8A5418 0%,#A5651A 55%,#F29A1E 100%);opacity:.85"></div>

  <!-- breaded wings -->
  <div class="dots" style="left:44px;top:50px"><i></i><i></i><i></i></div>
  <div class="t heading" style="left:43px;top:62px">BREADED WINGS</div>
  <div class="t note" style="left:46px;top:104px">ALL WINGS SERVIED WITH FRIES &amp; 1 dip</div>
  <div class="badge light" style="left:33px;top:123px;width:36px;height:36px">1</div>
  <div class="t lead" style="left:85px;top:133px">Wings <span>or</span> Boneless</div>
  <div class="badge light" style="left:34px;top:182px;width:36px;height:36px">2</div>
  <div class="t price-row" style="left:88px;top:181px"><b>4</b> Wings ...<b>6.99</b></div>
  <div class="t price-row" style="left:224px;top:182px"><b>8</b> Wings &nbsp;... <b>6.99</b></div>
  <div class="t price-row" style="left:88px;top:208px"><b>10</b> Wings ...<b>6.99</b></div>
  <div class="t price-row" style="left:224px;top:209px"><b>12</b> Wings... <b>6.99</b></div>

  <!-- tenders -->
  <div class="dots" style="left:44px;top:239px"><i></i><i></i><i></i></div>
  <div class="t heading sub" style="left:43px;top:255px">BUTTERMILK MARINATED</div>
  <div class="t heading sub" style="left:43px;top:284px">TENDERS</div>
  <div class="t note" style="left:46px;top:319px">ALL WINGS SERVIED WITH FRIES &amp; 1 dip</div>
  <div class="badge light" style="left:32px;top:344px;width:36px;height:36px">1</div>
  <div class="t lead" style="left:84px;top:358px">Large <span>or</span> Mini</div>
  <div class="badge light" style="left:33px;top:393px;width:36px;height:36px">2</div>
  <div class="t price-row" style="left:86px;top:393px"><b>3</b> Tenders</div>
  <div class="t price-row" style="left:190px;top:393px">... <b>5.99</b></div>
  <div class="t price-row" style="left:86px;top:422px"><b>6</b> Tenders</div>
  <div class="t price-row" style="left:191px;top:422px">... <b>8.99</b></div>

  <div class="badge dark" style="left:36px;top:460px;width:34px;height:34px">3</div>
  <div class="t tiny" style="left:83px;top:476px">Choose Your Flavors</div>
  <div class="t opt" style="left:46px;top:500px"><b>1.</b> Original <b>2.</b> Buffalo</div>
  <div class="t opt" style="left:197px;top:500px"><b>3.</b> Lemon Paper</div>
  <div class="t opt" style="left:46px;top:527px"><b>4.</b> Dynamite</div>
  <div class="t opt" style="left:142px;top:527px"><b>5.</b> Garlic Pameson</div>
  <div class="t opt" style="left:46px;top:557px"><b>6.</b> Nashville or Hotdamn</div>
  <div class="t opt" style="left:226px;top:557px"><b>7.</b> BBQ</div>

  <div class="badge dark" style="left:37px;top:580px;width:35px;height:35px">4</div>
  <div class="t tiny" style="left:83px;top:596px">Choose Your Sause</div>
  <div class="t opt" style="left:46px;top:628px"><b>1.</b> Blue Cheese</div>
  <div class="t opt" style="left:186px;top:629px"><b>1.</b> House Ranch</div>
  <div class="t opt" style="left:46px;top:662px"><b>1.</b> Roost Special</div>
  <div class="t opt" style="left:186px;top:662px"><b>1.</b> Honey Mustard</div>

  <!-- sandwich option bottom -->
  <div class="dots" style="left:44px;top:691px"><i></i><i></i><i></i></div>
  <div class="t heading" style="left:45px;top:704px">SANDWICH</div>
  <div class="t heading" style="left:45px;top:743px">OPTION 1</div>
  <div class="t note" style="left:46px;top:787px">ALL WINGS SERVIED WITH FRIES</div>
  <div class="t note" style="left:46px;top:801px">&amp; 1 dip</div>

  <div class="badge light" style="left:259px;top:699px;width:36px;height:36px">1</div>
  <div class="micro" style="left:303px;top:709px">Select your<br>base</div>
  <div class="desc" style="left:363px;top:706px;font-size:12px">Brioche bun , Soft Deli Roll,<br>Waffle, Double Chesney</div>
  <div class="badge light" style="left:260px;top:747px;width:36px;height:36px">2</div>
  <div class="micro" style="left:303px;top:756px">Select your<br>Chicken</div>
  <div class="desc" style="left:363px;top:753px;font-size:12px">Tenders,<br>Chicken Breasrt</div>

  <div class="badge dark" style="left:602px;top:703px;width:30px;height:30px;font-size:18px">3</div>
  <div class="t tiny" style="left:635px;top:717px;font-size:9px">Choose Your Flavors</div>
  <div class="t opt" style="left:633px;top:737px">1. Original &nbsp;1. Buffalo</div>
  <div class="t opt" style="left:633px;top:761px">2. Lemon Paper &nbsp;&nbsp;2. BBQ</div>
  <div class="t opt" style="left:633px;top:786px">2. Dynamite &nbsp;&nbsp;2. Garlic Pameson</div>
  <div class="t opt" style="left:633px;top:810px">2. Nashville or Hotdamn</div>

  <div class="badge dark" style="left:825px;top:703px;width:30px;height:30px;font-size:18px">4</div>
  <div class="t tiny" style="left:860px;top:717px;font-size:9px">Add Topping</div>
  <div class="t opt" style="left:860px;top:736px">1. Cheese</div>
  <div class="t opt" style="left:860px;top:760px">1. Lettuce</div>
  <div class="t opt" style="left:860px;top:786px">1. Slaw</div>
  <div class="t opt" style="left:860px;top:812px">1. Pickles</div>

  <div class="badge dark" style="left:1011px;top:703px;width:30px;height:30px;font-size:18px">5</div>
  <div class="t tiny" style="left:1045px;top:717px;font-size:9px">Choose Your Sause</div>
  <div class="t opt" style="left:1014px;top:736px">1. Blue Cheese</div>
  <div class="t opt" style="left:1014px;top:757px">1. Honey Mustard</div>
  <div class="t opt" style="left:1014px;top:777px">1. House Ranch</div>
  <div class="t opt" style="left:1014px;top:797px">1. Daynmaited</div>
  <div class="t opt" style="left:1014px;top:818px">1. Roost Special</div>

  <!-- slides -->
  <div class="dots" style="left:363px;top:230px"><i></i><i></i><i></i></div>
  <div class="t heading" style="left:363px;top:243px">SLIDES</div>
  <div class="t item" style="left:362px;top:298px">Chicken Popcorn .... <b>5.50</b></div>
  <div class="desc" style="left:362px;top:327px">Chicken pop corn topped with meltd<br>cheddar cheese, dynamite sasue, sismes</div>
  <div class="t item" style="left:362px;top:366px">Chilli &nbsp;Bites &nbsp;.... <b>5.50</b></div>
  <div class="desc" style="left:362px;top:395px">Chilli cheese bites , Select your dip</div>
  <div class="t item" style="left:362px;top:425px">Mozerla Stick</div>
  <div class="t item" style="left:557px;top:425px">.... <b>5.50</b></div>
  <div class="t item" style="left:362px;top:463px">Garlic Mushrooms</div>
  <div class="t item" style="left:362px;top:490px">Bites &nbsp;5.50</div>
  <div class="t item" style="left:362px;top:531px">Onion Rings</div>
  <div class="t item" style="left:557px;top:531px">.... <b>5.50</b></div>
  <div class="desc" style="left:362px;top:559px">Mac &amp; cheese bites Roost special<br>( mash potato, &nbsp;grave sause ) Honey mustard slaw</div>

  <div class="dots" style="left:363px;top:597px"><i></i><i></i><i></i></div>
  <div class="t heading" style="left:362px;top:605px">FRIES</div>
  <div class="desc" style="left:363px;top:644px">Seasoned Fries / Regular Fries / Cajuan Fries</div>
  <div class="desc" style="left:365px;top:665px">Haloomi Fries / Regular Sweet Potato</div>

  <!-- fries column -->
  <div class="dots" style="left:673px;top:228px"><i></i><i></i><i></i></div>
  <div class="t heading" style="left:672px;top:243px">FRIES</div>
  <div class="t item" style="left:672px;top:294px">Loaded Fries</div>
  <div class="desc" style="left:672px;top:321px">Fry by Chips loaded with<br>melted cheese , dynamite<br>sauce , jalapeño</div>
  <div class="t item" style="left:672px;top:373px">Take Loaded</div>
  <div class="desc" style="left:674px;top:400px">Chips loaded with melted<br>cheese, &nbsp;hot sauce , takes</div>
  <div class="t item" style="left:672px;top:452px">Chicketoos</div>
  <div class="desc" style="left:674px;top:479px">Chips tenders loaded with<br>melted cheese , ketchup,<br>crunchos</div>
  <div class="t item" style="left:672px;top:531px">Oh Hot Damn</div>
  <div class="desc" style="left:673px;top:557px">Chips nashville tender , melted<br>cheese , sriracha sauce , green<br>chilli pepper</div>
  <div class="t item" style="left:672px;top:610px">Pop Corn</div>
  <div class="desc" style="left:673px;top:636px">Chips Chicken pop corn ,<br>melted cheese , Daynmaited<br>sause , sesames</div>

  <!-- sandwich option right -->
  <div class="dots" style="left:882px;top:50px"><i></i><i></i><i></i></div>
  <div class="t heading" style="left:879px;top:63px">SANDWICH &nbsp;OPTION 1</div>
  <div class="t note" style="left:882px;top:103px">ALL WINGS SERVIED WITH FRIES &amp; 1 dip</div>

  <div class="t item" style="left:881px;top:143px">Classic burger ........... <b>5.50</b></div>
  <div class="desc" style="left:882px;top:173px">Fried chicken breast, fresh pickles &amp; creamy<br>mayo in a soft brioche bun</div>
  <div class="t item" style="left:881px;top:233px">Roost Special ............ <b>6.95</b></div>
  <div class="desc" style="left:883px;top:269px">Relish sauce, Fried chicken breast,Honey<br>mustard, Red cabbage in a soft brioche bun</div>
  <div class="t item" style="left:881px;top:318px">Nashville Oh</div>
  <div class="t item" style="left:881px;top:344px">Hot Damn</div>
  <div class="t item" style="left:1025px;top:341px">................ <b>7.99</b></div>
  <div class="desc" style="left:883px;top:372px">Fried nashville chicken breast, fresh pickles<br>&amp; roost sause, pot of grave&amp; mash potato</div>
  <div class="t item" style="left:881px;top:418px">Double Cheesy</div>
  <div class="t item" style="left:881px;top:445px">Toasted</div>
  <div class="t item" style="left:1025px;top:443px">................ <b>5.99</b></div>
  <div class="desc" style="left:883px;top:478px">Tenders ,Cheese, slaw, pickles, mayo</div>
  <div class="t item" style="left:881px;top:517px">Dynamite Burger ...... <b>6.95</b></div>
  <div class="desc" style="left:883px;top:548px">Sweet mayo, Iceberg lettuce, Fried chicken<br>breast, Dynamite sauce , &nbsp;soft deli rolls</div>
  <div class="t item" style="left:881px;top:603px">Mini fillet Slider &nbsp;&nbsp;&nbsp;&nbsp;...... <b>4.99</b></div>
  <div class="desc" style="left:882px;top:628px">(lemon herbs , Deled peri peri , mango lime)</div>
  <div class="desc" style="left:882px;top:649px">Mini Fillet , lettuce , Cheese , Select your<br>flavour in a mini bun</div>

</main>
</body>
</html>
```